Business Card Design needed for logo design project

This project is linked to Consulting Firm + Meeting Space needs logo and bus card..
Our company needs a Business Card Design. Please refer to our original project in the link above.
Industry/Entity Type
Business

```html
<!DOCTYPE html>
<html lang="en">
<head>
<meta charset="utf-8">
<title>Talvenne Business Card</title>
<link href="https://fonts.googleapis.com/css2?family=Questrial&display=swap" rel="stylesheet">
<style>
  :root {
    --backdrop: #ececec;
    --card: #f7f7f7;
    --brand-blue: #1f7cc6;
    --deep-navy: #23307f;
    --ink-blue: #2a62b4;
    --shadow: rgba(0, 0, 0, 0.12);
  }
  * { margin: 0; padding: 0; box-sizing: border-box; }
  html, body {
    width: 1200px; height: 675px; overflow: hidden;
    background: var(--backdrop);
    font-family: "Questrial", "Century Gothic", sans-serif;
  }
  .stage {
    position: relative; width: 1200px; height: 675px;
    display: flex; justify-content: center; align-items: center; gap: 60px;
  }
  .card {
    position: relative; width: 500px; height: 286px;
    background: var(--card);
    box-shadow: 0 6px 18px var(--shadow);
  }
  .card-front {
    display: flex; align-items: center; justify-content: center;
  }
  .front-name { color: var(--brand-blue); font-size: 40px; letter-spacing: 0.5px; }
  .address {
    position: absolute; left: 262px; top: 42px;
    color: var(--brand-blue); font-size: 13px; line-height: 1.3;
  }
  .contact-list {
    position: absolute; left: 262px; top: 98px;
    list-style: none; color: var(--brand-blue); font-size: 13px; line-height: 1.35;
  }
  .contact-list li { display: flex; align-items: center; gap: 6px; }
  .contact-list svg { width: 10px; height: 10px; fill: var(--deep-navy); flex: none; }
  .brand-name {
    position: absolute; left: 30px; bottom: 30px;
    color: var(--brand-blue); font-size: 40px; letter-spacing: 0.5px;
  }
  .person {
    position: absolute; left: 262px; bottom: 58px;
  }
  .person-name { color: var(--deep-navy); font-size: 13px; font-weight: 700; letter-spacing: 0.3px; }
  .person-title { color: var(--ink-blue); font-size: 12px; }
</style>
</head>
<body>
<main class="stage">
  <section class="card card-front">
    <div class="front-name">Talvenne</div>
  </section>

  <section class="card card-back">
    <p class="address">4410 Alder Park Way Suite 200,<br>Lakeview USA 90412</p>
    <ul class="contact-list">
      <li><svg viewBox="0 0 10 10"><path d="M2 0.5 L3.6 2.4 L2.8 3.6 Q4 6 6.4 7.2 L7.6 6.4 L9.5 8 L8.4 9.5 Q3 9 0.5 1.6 Z"/></svg>555.014.2280</li>
      <li><svg viewBox="0 0 10 10"><rect x="2.5" y="0.5" width="5" height="3"/><rect x="0.5" y="3.5" width="9" height="4" rx="1"/><rect x="2.5" y="6.5" width="5" height="3"/></svg>555.014.2281</li>
      <li><svg viewBox="0 0 10 10"><path d="M0.5 2 H9.5 V8.5 H0.5 Z M1 2.5 L5 5.6 L9 2.5" fill="none" stroke="#23307f" stroke-width="1"/></svg>hello@talvenne.example</li>
      <li><svg viewBox="0 0 10 10"><g fill="none" stroke="#23307f" stroke-width="0.9"><circle cx="5" cy="5" r="4.3"/><ellipse cx="5" cy="5" rx="1.9" ry="4.3"/><path d="M0.7 5 H9.3"/></g></svg>www.talvenne.example</li>
    </ul>
    <div class="person">
      <div class="person-name">EMPLOYEE NAME</div>
      <div class="person-title">Title</div>
    </div>
    <div class="brand-name">Talvenne</div>
  </section>
</main>
</body>
</html>
```